Corvane Property Group Business cards

I am starting a property development and consultancy business called Corvane Property Group. I have a logo designed and a website on its way:
www.corvanegroup-example.com.au

I need a business card with the following:

Front:
Mostly orange with logo taking up all front of card

Back of card:
Logo

Mark Dellaway
Managing Director

T +61 452 907 364
E mark.dellaway@corvanegroup-example.com.au
www.corvanegroup-example.com.au

Industry/Entity Type

Business

Requirements
Must have
• curved edges

```html
<!DOCTYPE html>
<html lang="en">
<head>
<meta charset="utf-8">
<title>Corvane Property Group – Business Cards</title>
<link rel="stylesheet" href="https://fonts.googleapis.com/css2?family=Arimo:wght@400&display=swap">
<style>
  :root {
    --backdrop: #2e2e2e;
    --brand-orange: #f9ad1e;
    --card-white: #ffffff;
    --text-grey: #5a5a5a;
    --text-dark: #4a4a4a;
  }
  * { margin: 0; padding: 0; box-sizing: border-box; }
  html, body {
    width: 1200px;
    height: 900px;
    overflow: hidden;
    background: var(--backdrop);
    font-family: "Arimo", Arial, sans-serif;
  }
  .canvas {
    position: relative;
    width: 1200px;
    height: 900px;
  }
  .card {
    position: absolute;
    width: 600px;
    height: 370px;
    border-radius: 12px;
    overflow: hidden;
  }
  .card-front {
    left: 212px;
    top: 60px;
    background: var(--brand-orange);
    display: flex;
    align-items: center;
    justify-content: center;
  }
  .card-front .brand-name {
    color: var(--card-white);
    font-size: 44px;
    font-weight: 400;
    letter-spacing: 1px;
  }
  .card-back {
    left: 388px;
    top: 470px;
    background: var(--card-white);
  }
  .card-back .brand-name {
    position: absolute;
    left: 32px;
    top: 40px;
    color: var(--brand-orange);
    font-size: 24px;
    font-weight: 400;
  }
  .contact-person {
    position: absolute;
    right: 34px;
    top: 118px;
    text-align: right;
  }
  .person-name {
    color: var(--brand-orange);
    font-size: 28px;
    line-height: 1.1;
  }
  .person-title {
    color: var(--text-grey);
    font-size: 16px;
    margin-top: 4px;
  }
  .contact-band {
    position: absolute;
    left: 0;
    right: 0;
    top: 205px;
    height: 74px;
    background: var(--brand-orange);
    display: flex;
    align-items: center;
    justify-content: space-between;
    padding: 0 34px;
    color: var(--text-dark);
    font-size: 15px;
  }
  .contact-label { margin-right: 10px; }
  .website {
    position: absolute;
    left: 0;
    right: 0;
    top: 308px;
    text-align: center;
    color: var(--text-grey);
    font-size: 17px;
  }
</style>
</head>
<body>
  <main class="canvas">
    <section class="card card-front" aria-label="Card front">
      <p class="brand-name">Corvane Property Group</p>
    </section>

    <section class="card card-back" aria-label="Card back">
      <p class="brand-name">Corvane Property Group</p>
      <div class="contact-person">
        <p class="person-name">Mark Dellaway</p>
        <p class="person-title">Managing Director</p>
      </div>
      <div class="contact-band">
        <p class="contact-phone"><span class="contact-label">T :</span>+61 452 907 364</p>
        <p class="contact-email"><span class="contact-label">E :</span>mark.dellaway@corvanegroup-example.com.au</p>
      </div>
      <p class="website">www.corvanegroup-example.com.au</p>
    </section>
  </main>
</body>
</html>
```